Business Card Design Project

TRK Solutions is a Electrical and Communications Services and Maintenance contractor to the Mining Oil and Gas sectors of Australia.
Our clients will be planners, Schedulers, Tradespeople and Engineers

We are yet to determine the primary colours that we will use on the business cards but the logos attached will form foundation of the colours used for logos on Business cards, Website, Uniforms, vehicles etc.

Target Market(s)

Mining engineers and shedulers

Industry/Entity Type

Contractor

Requirements
Must have
• information to be included on the card

Name: Derek Hanley
Title: Managing Director
Company: TRK Solutions Pty Ltd
Phone: 08 9YYY YYYY
Mobile 0400 813 942
email: dhanley@trksolutions-example.com
Website www.trksolutions-example.com

Address: U5/7 Bexley Street Kelmscott, SA 5112
Postal Address: PO Box 4187 Kelmscott SA 5113

Nice to have
• Double sided. Maybe the logo on the back

```html
<!DOCTYPE html>
<html lang="en">
<head>
<meta charset="utf-8">
<title>TRK Solutions – Business Card</title>
<link rel="stylesheet" href="https://fonts.googleapis.com/css2?family=Exo+2:wght@300;400;600&display=swap">
<style>
  :root {
    --backdrop: #8c8c8c;
    --navy: #0d1a36;
    --navy-glow: #1f3a66;
    --white: #ffffff;
    --orange: #f39a1e;
    --card-font: "Exo 2", Arial, sans-serif;
  }
  * { box-sizing: border-box; margin: 0; padding: 0; }
  html, body { width: 1200px; height: 900px; overflow: hidden; }
  body {
    background: var(--backdrop);
    font-family: var(--card-font);
    color: var(--white);
    position: relative;
  }
  .card {
    position: absolute;
    width: 680px;
    height: 390px;
    background: radial-gradient(ellipse 50% 50% at 50% 45%, var(--navy-glow) 0%, var(--navy) 75%);
  }
  .card--front { left: 80px; top: 40px; }
  .card--back {
    left: 440px; top: 466px;
    background: radial-gradient(ellipse 40% 45% at 42% 40%, var(--navy-glow) 0%, var(--navy) 75%);
  }

  .brand { position: absolute; left: 0; right: 0; text-align: center; }
  .brand__name {
    display: inline-flex; align-items: center; gap: 14px;
    font-weight: 400; color: var(--white); line-height: 1; letter-spacing: 2px;
  }
  .brand__dot { display: inline-block; border-radius: 50%; background: var(--orange); }

  .card--front .brand { top: 150px; }
  .card--front .brand__name { font-size: 66px; }
  .card--front .brand__dot { width: 18px; height: 18px; }
  .front__web {
    position: absolute; left: 0; right: 0; top: 298px; text-align: center;
    color: var(--orange); font-weight: 600; font-size: 18px; letter-spacing: 1.5px;
  }

  .card--back .brand { top: 42px; }
  .card--back .brand__name { font-size: 44px; gap: 10px; }
  .card--back .brand__dot { width: 12px; height: 12px; }

  .person { position: absolute; left: 96px; top: 168px; }
  .person__name { font-size: 38px; font-weight: 300; letter-spacing: 1px; line-height: 1; }
  .person__title { font-size: 20px; font-weight: 300; margin-top: 4px; }
  .person__email { font-size: 15px; color: var(--orange); margin-top: 14px; }

  .contact { position: absolute; left: 424px; top: 174px; font-size: 17px; line-height: 1.15; }
  .contact__label { color: var(--orange); font-weight: 600; }
  .contact__value { margin-bottom: 6px; }

  .address {
    position: absolute; left: 0; right: 0; top: 308px; text-align: center;
    font-size: 14px; line-height: 1.6;
  }
  .address__bullet { color: var(--orange); margin: 0 6px; }
</style>
</head>
<body>
  <section class="card card--front" aria-label="Business card front">
    <div class="brand"><span class="brand__name">TRK Solutions<span class="brand__dot"></span></span></div>
    <p class="front__web">www.trksolutions-example.com</p>
  </section>

  <section class="card card--back" aria-label="Business card back">
    <div class="brand"><span class="brand__name">TRK Solutions<span class="brand__dot"></span></span></div>

    <div class="person">
      <p class="person__name">Derek Hanley</p>
      <p class="person__title">Managing Director</p>
      <p class="person__email">dhanley@trksolutions-example.com</p>
    </div>

    <div class="contact">
      <p class="contact__label">Phone</p>
      <p class="contact__value">08 9YYY YYYY</p>
      <p class="contact__label">Mobile</p>
      <p class="contact__value">0400 813 942</p>
    </div>

    <div class="address">
      <p><span class="address__bullet">•</span>TRK Solutions Pty Ltd, U5/7 Bexley Street Kelmscott, SA 5112<span class="address__bullet">•</span></p>
      <p><span class="address__bullet">•</span>PO Box 4187 Kelmscott SA 5113<span class="address__bullet">•</span></p>
    </div>
  </section>
</body>
</html>
```